Redesign Of Flower Delivery Subscription Service Website

I need a revamped website of www.petal-rush.com

Please revamp current design using same content....

Target Market(s)

people who buy flowers. Brides, wedding planners, wedding photographer, married man, boyfriend, etc.

Industry/Entity Type

Florist

Number of Pages Required

5+ page

Colors

Designer to choose colors to be used in the design.

Requirements
Must have
• I need a revamped website of www.petal-rush.com
• Please revamp current design using same content....
Nice to have
Should not have

```html
<!DOCTYPE html>
<html lang="en">
<head>
<meta charset="utf-8">
<title>Petal Rush – Landing Page</title>
<link rel="stylesheet" href="https://fonts.googleapis.com/css2?family=Josefin+Sans:wght@400;600;700&family=Lora:ital,wght@0,400;0,700;1,400&display=swap">
<style>
:root{
  --green:#94c43c;
  --ink:#1e1e1e;
  --page:#fafafa;
  --paper:#ffffff;
  --dark:#2a2625;
  --orange:#f9a124;
  --pink:#f88b86;
}
*{box-sizing:border-box;margin:0;padding:0}
html,body{width:1200px;height:1200px;overflow:hidden;background:var(--paper)}
body{position:relative;font-family:"Josefin Sans",sans-serif;color:var(--ink)}
.abs{position:absolute}
.decor{position:absolute;left:0;top:0;width:1200px;height:1200px}
.side-label{position:absolute;left:178px;top:916px;writing-mode:vertical-rl;font-family:Lora,serif;font-size:10px;letter-spacing:.5px;color:#9a9a9a;line-height:14px}

.page{position:absolute;overflow:hidden;background:var(--page)}
.page--main{left:218px;top:86px;width:559px;height:1114px;box-shadow:0 10px 40px rgba(0,0,0,.08);z-index:2}
.page--full{left:733px;top:0;width:249px;height:1200px;box-shadow:0 6px 30px rgba(0,0,0,.07);z-index:1}
.page .abs{position:absolute}

.photo{position:absolute}
.photo--bride{background:linear-gradient(160deg,#6f7a55 0%,#c9b7a3 30%,#e9ece3 55%,#b9c8a8 80%,#7e936a 100%)}
.photo--tulips{background:linear-gradient(180deg,#f4f2ef 0%,#e6e6ea 35%,#7a79b8 60%,#5a8a48 85%,#f2f2f2 100%)}
.photo--tulip-dark{background:radial-gradient(circle at 50% 45%,#d4652a 0%,#8c3a1c 12%,#2c2725 34%,var(--dark) 100%)}
.photo--gift{background:radial-gradient(circle at 50% 70%,#e0416e 0%,#6a2230 25%,#2b2020 55%,#1b1616 100%)}
.photo--purple{background:linear-gradient(120deg,#a27a6f 0%,#7d7bb4 35%,#9b93cf 60%,#c07a6a 100%)}
.photo--wreath{background:radial-gradient(circle at 50% 50%,#f29a8a 0%,#e36d63 30%,#7f9a5a 60%,#4f6d38 100%)}
.photo--band{background:linear-gradient(90deg,#f3f3f3 0%,#f0e2d6 55%,#f5e6d8 75%,#f3f3f3 100%)}

.hamburger{left:19px;top:33px;width:9px}
.hamburger span{display:block;height:1.5px;background:var(--ink);margin-bottom:1.5px}
.brand{text-align:left;font-weight:400;color:#5b5b5b;white-space:nowrap}
.brand .name{font-size:15px;letter-spacing:1.5px;line-height:16px}
.brand .tag{font-size:4.5px;letter-spacing:.3px;color:#7a7a7a}
.socials{display:flex;gap:15px}
.socials span{width:12px;height:12px;border-radius:50%;background:var(--green)}
.offer{font-size:6px;letter-spacing:.6px;color:#8f8f8f;white-space:nowrap}
.offer b{font-weight:400;display:inline-block;width:12px;height:1px;background:#bbb;vertical-align:middle;margin:0 6px}

.headline{color:var(--green);font-weight:700;letter-spacing:2px;white-space:nowrap}
.perk{background:var(--paper);padding:9px 11px;display:flex;justify-content:space-between;align-items:center}
.perk h4{font-size:9px;font-weight:600;letter-spacing:.2px}
.perk p{font-size:4.5px;letter-spacing:.3px;color:#555;margin-top:2px}
.perk svg{width:12px;height:12px}
.play{border-radius:50%;background:linear-gradient(160deg,var(--pink) 0%,var(--orange) 100%);display:flex;align-items:center;justify-content:center;color:#fff;font-size:9px;font-weight:600;gap:5px}

.card{background:var(--paper)}
.h2{font-weight:600;letter-spacing:.6px;color:var(--ink)}
.body{font-family:Lora,serif;color:#333}
.body b{font-weight:700}
.hl{color:var(--green)}

.email{display:flex;border:1.5px solid var(--green);background:var(--paper)}
.email .field{flex:1;font-size:4.5px;color:var(--green);letter-spacing:.4px;padding-left:12px;display:flex;align-items:center}
.email .submit{background:var(--green);color:#fff;font-size:4.5px;font-weight:700;letter-spacing:.4px;display:flex;align-items:center;justify-content:center}
.tick{position:absolute;width:1px;height:5px;background:var(--green)}
</style>
</head>
<body>

<svg class="decor" viewBox="0 0 1200 1200" aria-hidden="true">
  <circle cx="272" cy="424" r="240" fill="none" stroke="#ececec" stroke-width="1"/>
</svg>

<div class="side-label">PETAL RUSH V1<br>LANDING PAGE MOCKUP</div>

<!-- full-length page preview -->
<section class="page page--full">
  <div class="abs brand" style="left:100px;top:10px"><div class="name" style="font-size:6px;line-height:7px;letter-spacing:.5px">PETAL RUSH</div><div class="tag" style="font-size:2.2px">Harbor City Flower Company</div></div>
  <div class="abs offer" style="left:160px;top:13px;font-size:2.6px;letter-spacing:.2px">FREE DELIVERY — now only $69.95/MTH</div>
  <div class="abs socials" style="left:199px;top:3px;gap:7px"><span style="width:5px;height:5px"></span><span style="width:5px;height:5px"></span><span style="width:5px;height:5px"></span><span style="width:5px;height:5px"></span></div>

  <div class="photo photo--bride" role="img" aria-label="Bride holding a white bouquet" style="left:0;top:72px;width:205px;height:116px"></div>
  <div class="abs headline" style="left:107px;top:38px;font-size:44px;line-height:44px">ALWAYS</div>
  <div class="abs headline" style="left:183px;top:74px;font-size:44px;line-height:44px">FREE</div>
  <div class="abs card" style="left:60px;top:106px;width:55px;height:14px"></div>
  <div class="abs card" style="left:121px;top:106px;width:55px;height:14px"></div>
  <div class="abs play" style="left:187px;top:142px;width:48px;height:48px;font-size:4px">▸ Play</div>

  <div class="photo photo--tulips" role="img" aria-label="Red tulips with purple hyacinths" style="left:44px;top:166px;width:56px;height:68px"></div>
  <div class="abs card" style="left:38px;top:234px;width:62px;height:110px"></div>
  <div class="photo photo--tulip-dark" role="img" aria-label="Single orange tulip on a dark background" style="left:100px;top:226px;width:66px;height:57px"></div>
  <div class="abs h2" style="right:28px;top:203px;font-size:8px">Set it and forget it</div>
  <div class="abs body" style="left:177px;top:223px;width:62px;font-size:3px;line-height:5px">PetalRush is a set it and forget it subscription based flower delivery service.<br><br>For an amazing price we hand deliver a gorgeous arrangement to anyone you want every month.</div>

  <div class="abs h2" style="left:97px;top:309px;font-size:6.5px;line-height:10px;text-align:right;width:75px">Making Someone's<br>day better</div>
  <div class="abs body" style="left:105px;top:340px;width:55px;font-size:3px;line-height:5px">Be the hero in that special someone's life each month. It feels good to make a difference.</div>
  <div class="photo photo--gift" role="img" aria-label="Man holding a wrapped bouquet at night" style="left:161px;top:331px;width:77px;height:70px"></div>

  <div class="abs email" style="left:111px;top:429px;width:82px;height:7px;border-width:1px"><div class="field" style="font-size:2px;padding-left:5px">NAME@EMAIL.COM</div><div class="submit" style="width:22px;font-size:2px">SUBMIT</div></div>

  <div class="photo photo--band" role="img" aria-label="Soft blurred flower arrangement" style="left:44px;top:466px;width:190px;height:78px"></div>
  <div class="abs h2" style="left:-4px;top:484px;font-size:7px;line-height:11px">Monthly <span class="hl">Subscription</span><br><span class="hl">Based</span> Flower Delivery<br>Service in <span class="hl">Bayview - CA</span><br>By Our Florist Shop</div>
  <div class="abs body" style="left:44px;top:550px;width:115px;font-size:2.6px;line-height:5.4px"><span class="hl" style="font-size:10px;float:left;line-height:10px;margin-right:2px">E</span>very moment of life could be cherished with flowers. Our monthly subscription delivers fresh, hand designed arrangements to the ones you love. Choose the size, set the dates and let our florists handle every detail, from seasonal blooms to classic roses, delivered right on time to their door.</div>

  <div class="photo photo--purple" role="img" aria-label="Field of purple and pink tulips" style="left:44px;top:650px;width:205px;height:204px"></div>
  <div class="abs card" style="left:77px;top:630px;width:111px;height:212px;background:rgba(255,255,255,.93)"></div>
  <div class="abs headline" style="left:95px;top:622px;font-size:44px;color:#eeeeee">03</div>
  <div class="abs h2" style="left:89px;top:662px;font-size:4.5px;line-height:6.5px">Get Yourself Subscribed And<br>Claim <span class="hl">Discounts</span> On Big<br>Orders!</div>
  <div class="abs body" style="left:89px;top:692px;width:84px;font-size:2.6px;line-height:5.5px">Get love and adulation by gifting flowers to your loved ones on special occasions. Follow the subscription criteria and get your hands on the most valuable service for all kinds of events. Select the right delivery dates and we will deliver your flowers on the exact special day to make your loved one smile.</div>
  <div class="abs" style="left:89px;top:820px;width:6px;height:6px;border:.5px solid #ccc"></div>
  <div class="abs" style="left:96px;top:820px;width:6px;height:6px;background:var(--green)"></div>

  <div class="abs" style="left:111px;top:871px;font-size:4px;letter-spacing:.3px">inspiration</div>
  <div class="photo photo--wreath" role="img" aria-label="Pink rose wreath on grass" style="left:89px;top:910px;width:72px;height:100px"></div>
  <div class="abs headline" style="left:50px;top:941px;font-size:14px;letter-spacing:.5px;font-weight:600">Set It</div>
  <div class="abs headline" style="left:145px;top:969px;font-size:14px;letter-spacing:.5px;font-weight:600">Forget it</div>
  <div class="abs" style="left:122px;top:1018px;width:39px;height:7px;border:1px solid var(--green)"></div>

  <div class="abs brand" style="left:103px;top:1068px"><div class="name" style="font-size:6px;line-height:7px;letter-spacing:.5px">PETAL RUSH</div><div class="tag" style="font-size:2.2px">Harbor City Flower Company</div></div>
  <div class="abs socials" style="left:103px;top:1095px;gap:6px"><span style="width:5px;height:5px"></span><span style="width:5px;height:5px"></span><span style="width:5px;height:5px"></span><span style="width:5px;height:5px"></span></div>
  <div class="abs body" style="left:48px;top:1084px;font-size:2.4px;line-height:4px;color:#666">Privacy Policy<br>Terms and Conditions<br>Site Credits</div>
  <div class="abs body" style="left:168px;top:1074px;font-size:2.4px;line-height:4px;color:#666;text-align:center">Contact Us<br>12 Harbor Lane, Bayview CA<br>Tel: 555 0142 0199<br>hello@petal-rush.com</div>
  <div class="abs" style="left:129px;top:1138px;font-size:2.4px;color:#666">RECEIVE A FREE UPGRADE</div>
  <div class="abs email" style="left:89px;top:1152px;width:72px;height:7px;border-width:1px"><div class="field" style="font-size:2px;padding-left:4px">NAME@EMAIL.COM</div><div class="submit" style="width:18px;font-size:2px">SUBMIT</div></div>
  <div class="abs" style="left:115px;top:1176px;font-size:2.4px;color:#888">© 2018 www.petal-rush.com</div>
</section>

<!-- landing page -->
<section class="page page--main">
  <div class="abs hamburger"><span></span><span></span><span></span></div>
  <div class="abs brand" style="left:226px;top:24px"><div class="name">PETAL RUSH</div><div class="tag">Harbor City Flower Company</div></div>
  <div class="abs socials" style="left:442px;top:5px"><span></span><span></span><span></span><span></span></div>
  <div class="abs offer" style="left:360px;top:29px">FREE DELIVERY<b></b>now only $69.95/MTH ($100 value)</div>
  <span class="tick" style="left:112px;top:92px"></span>

  <div class="photo photo--bride" role="img" aria-label="Bride smelling a white and green bouquet" style="left:0;top:160px;width:460px;height:244px"></div>
  <div class="abs headline" style="left:242px;top:100px;font-size:80px;line-height:80px">ALWAYS</div>
  <div class="abs headline" style="left:413px;top:182px;font-size:80px;line-height:80px">FREE</div>

  <div class="abs perk" style="left:25px;top:236px;width:123px;height:34px"><div><h4>Free Vase</h4><p>LEARN MORE</p></div>
    <svg viewBox="0 0 12 12"><path d="M4 1h4M5 1v3L3.5 7v3.5h5V7L7 4V1" fill="none" stroke="#333" stroke-width=".8"/></svg></div>
  <div class="abs perk" style="left:156px;top:236px;width:124px;height:34px"><div><h4>Free Delivery</h4><p>LEARN MORE</p></div>
    <svg viewBox="0 0 12 12"><path d="M1 3h7v5H1zM8 5h2l1.5 1.5V8H8" fill="none" stroke="#333" stroke-width=".8"/><circle cx="3" cy="9" r="1" fill="none" stroke="#333" stroke-width=".8"/><circle cx="9.5" cy="9" r="1" fill="none" stroke="#333" stroke-width=".8"/></svg></div>
  <div class="abs perk" style="left:288px;top:236px;width:124px;height:34px"><div><h4>Free Upgrade</h4><p>LEARN MORE</p></div>
    <svg viewBox="0 0 12 12"><circle cx="5.5" cy="5.5" r="4" fill="none" stroke="#333" stroke-width=".8"/><path d="M8.5 8.5l2.5 2.5M5.5 3.5v4M3.5 5.5h4" stroke="#333" stroke-width=".8"/></svg></div>

  <div class="abs play" style="left:417px;top:317px;width:109px;height:109px">▸ Play</div>

  <div class="abs card" style="left:25px;top:462px;width:174px;height:300px"></div>
  <div class="photo photo--tulips" role="img" aria-label="Red tulips and purple hyacinths in a white vase" style="left:50px;top:369px;width:174px;height:157px"></div>
  <div class="photo photo--tulip-dark" role="img" aria-label="Single orange tulip against a dark background" style="left:199px;top:477px;width:173px;height:156px"></div>
  <div class="abs" style="left:199px;top:477px;width:74px;height:12px;background:var(--dark);transform:translateY(-12px);clip-path:inset(0 0 0 0)"></div>

  <div class="abs h2" style="right:63px;top:456px;font-size:18px">Set it and forget it</div>
  <div class="abs body" style="left:397px;top:503px;width:120px;font-size:7.6px;line-height:12.4px">PetalRush is a <b>“SET IT and FORGET IT”</b> subscription based flower delivery service.<br><br>For an Amazing price PetalRush will hand deliver a gorgeous arrangement directly to anyone you want every month without you having to worry about it.</div>

  <div class="abs h2" style="left:51px;top:563px;font-size:18px;line-height:24px">But never<br>forget again</div>
  <div class="abs body" style="left:62px;top:634px;width:110px;font-size:7.4px;line-height:12.4px;text-align:right">When setting up your account, you can choose <b>exact delivery dates</b> for the months that have special days such as your Anniversary, Birthday, Valentines Day and Mothers Day. You might forget but we won't, <b>we have got ya covered!</b></div>

  <div class="abs h2" style="left:200px;top:691px;width:182px;font-size:18px;line-height:24px;text-align:right">Making Someone's<br>day better</div>
  <div class="abs body" style="left:236px;top:761px;width:112px;font-size:7.4px;line-height:12.4px">Be the <b>hero</b> in that special someone's life each and every month.<br><br>It feels good <b>to make a difference</b> in your loved ones day.</div>
  <div class="photo photo--gift" role="img" aria-label="Man holding a pink wrapped bouquet on a city street at night" style="left:360px;top:740px;width:174px;height:156px"></div>
  <span class="tick" style="left:265px;top:645px"></span>
  <span class="tick" style="left:347px;top:875px"></span>

  <div class="abs h2" style="left:60px;top:951px;width:152px;font-size:12px;line-height:17px;text-align:right">Enter Your Email To<br>Receive A Free Upgrade</div>
  <div class="abs email" style="left:248px;top:957px;width:185px;height:20px"><div class="field">NAME@EMAIL.COM</div><div class="submit" style="width:50px">SUBMIT</div></div>
  <span class="tick" style="left:447px;top:1019px"></span>

  <div class="photo photo--band" role="img" aria-label="Soft blurred floral arrangement" style="left:62px;top:1044px;width:435px;height:70px;background:linear-gradient(90deg,#f2f2f2,#efefef)"></div>
  <div class="abs h2" style="left:88px;top:1083px;font-size:18px;line-height:24px;white-space:nowrap">Monthly <span class="hl">Subscription</span><br><span class="hl">Based</span> Flower Delivery</div>
</section>

</body>
</html>
```